The name of my company is Tolmen Refacing LLC and I would like the sub text to say "Cabinet Refacing and Countertops". Have my name Dorian Tolmen, Owner / Sales, contact info: Cell: 360-555-0147 / Email: dorian.tolmen@quenmail.com

Simple, Clean, and Organized. With colors that will appeal to the eye.

Target Market(s)

Houses and Apartments

Industry/Entity Type

Cabinet Refacing

Contact Information for Business Card

Company name and sub text Dorian Tolmen - Owner / Sales, my cell phone number and email

Requirements
Must have
• Business name, my name / position, and my contact info
Nice to have
• Simple. Organized. Appealing to the eye

```html
<!DOCTYPE html>
<html lang="en">
<head>
<meta charset="utf-8">
<title>Tolmen Refacing LLC – Business Card</title>
<link rel="stylesheet" href="https://fonts.googleapis.com/css2?family=Questrial&family=Quicksand:wght@600&display=swap">
<style>
  :root {
    --backdrop: #e0e0e0;
    --card: #ffffff;
    --band: #436cb3;
    --brand-name: #8390ac;
    --ink: #333333;
    --tagline: #2a2a2a;
  }
  * { margin: 0; padding: 0; box-sizing: border-box; }
  html, body { width: 1200px; height: 1200px; overflow: hidden; }
  body {
    background: var(--backdrop);
    position: relative;
    font-family: "Questrial", sans-serif;
  }
  .card {
    position: absolute;
    background: var(--card);
    box-shadow: 6px 8px 14px rgba(0,0,0,0.35);
    overflow: hidden;
  }
  .card--front { left: 188px; top: 91px; width: 823px; height: 473px; }
  .card--back  { left: 186px; top: 635px; width: 828px; height: 474px; }
  .band { position: absolute; left: 0; right: 0; height: 25px; background: var(--band); }
  .band--top { top: 0; }
  .band--bottom { bottom: 0; }

  .brand { position: absolute; text-align: center; }
  .brand__mark { display: block; margin: 0 auto; background: var(--band); }
  .brand__name {
    color: var(--brand-name);
    font-family: "Questrial", sans-serif;
    font-weight: 400;
    white-space: nowrap;
    letter-spacing: 0.01em;
  }
  .brand__tagline {
    color: var(--tagline);
    font-family: "Quicksand", sans-serif;
    font-weight: 600;
    white-space: nowrap;
  }

  .card--front .brand { left: 50px; top: 170px; width: 350px; }
  .card--front .brand__mark { width: 54px; height: 54px; margin-bottom: 22px; }
  .card--front .brand__name { font-size: 31px; line-height: 36px; }
  .card--front .brand__tagline { font-size: 15px; margin-top: 8px; }

  .divider {
    position: absolute; left: 413px; top: 164px;
    width: 2px; height: 146px; background: var(--band);
  }

  .contact { position: absolute; left: 455px; top: 160px; }
  .contact__name {
    color: var(--band); font-size: 42px; line-height: 46px;
    letter-spacing: 0.01em; white-space: nowrap;
  }
  .contact__role { color: var(--ink); font-size: 24px; margin-top: 2px; white-space: nowrap; }
  .contact__list { list-style: none; margin-top: 20px; }
  .contact__item {
    display: flex; align-items: center; gap: 10px;
    color: var(--ink); font-size: 25px; line-height: 32px; white-space: nowrap;
  }
  .contact__item svg { width: 19px; height: 19px; flex: none; fill: var(--band); }

  .card--back .brand { left: 0; right: 0; top: 130px; }
  .card--back .brand__mark { width: 96px; height: 96px; margin-bottom: 34px; }
  .card--back .brand__name { font-size: 50px; line-height: 56px; }
  .card--back .brand__tagline { font-size: 25px; margin-top: 12px; }
</style>
</head>
<body>
  <section class="card card--front">
    <div class="band band--top"></div>
    <div class="brand">
      <span class="brand__mark"></span>
      <p class="brand__name">TOLMEN REFACING, LLC</p>
      <p class="brand__tagline">Cabinets and Countertops</p>
    </div>
    <div class="divider"></div>
    <div class="contact">
      <h1 class="contact__name">DORIAN TOLMEN</h1>
      <p class="contact__role">Owner I Sales</p>
      <ul class="contact__list">
        <li class="contact__item">
          <svg viewBox="0 0 24 24" aria-hidden="true"><path d="M6.6 10.8c1.4 2.8 3.8 5.1 6.6 6.6l2.2-2.2c.3-.3.7-.4 1-.2 1.1.4 2.3.6 3.6.6.6 0 1 .4 1 1V20c0 .6-.4 1-1 1C10.6 21 3 13.4 3 4c0-.6.4-1 1-1h3.5c.6 0 1 .4 1 1 0 1.3.2 2.5.6 3.6.1.3 0 .7-.2 1z"/></svg>
          <span>360-555-0147</span>
        </li>
        <li class="contact__item">
          <svg viewBox="0 0 24 24" aria-hidden="true"><path d="M2 5h20v14H2z M3.5 6.5 12 13l8.5-6.5z" fill-rule="evenodd"/></svg>
          <span>dorian.tolmen@quenmail.com</span>
        </li>
      </ul>
    </div>
    <div class="band band--bottom"></div>
  </section>

  <section class="card card--back">
    <div class="band band--top"></div>
    <div class="brand">
      <span class="brand__mark"></span>
      <p class="brand__name">TOLMEN REFACING, LLC</p>
      <p class="brand__tagline">Cabinets and Countertops</p>
    </div>
    <div class="band band--bottom"></div>
  </section>
</body>
</html>
```